Independence Day Graphics for Sale

I want to create 10 social media graphics (new Pictora size 4:5 (1080 x 1350 pixels) focusing on our July 4th Sale Graphics, using any of the pics attached. Use the attached pics, NO RANDOM STOCK PHOTOGRAPHY. For the color scheme of the graphics, they should all be complementary to the product colors in the photos.
You can add any of the photos attached but none are required. You can do some of the graphics in all text. I mainly need BOLD text that says one of the headlines (10 total) SEE ATTACHED WORD DOCUMENT for the headlines to use.

Target Market(s)

women looking to lose weight

Requirements
Must have
• pics attached and text attached

```html
<!DOCTYPE html>
<html lang="en">
<head>
<meta charset="utf-8">
<title>July 4th Sale Social Graphics</title>
<link href="https://fonts.googleapis.com/css2?family=League+Spartan:wght@700;800&display=swap" rel="stylesheet">
<style>
  :root {
    --red: #d1282f;
    --blue: #2559b2;
    --white: #ffffff;
    --navy-deep: #12245a;
    --photo-light: #e9e8e6;
    --photo-mid: #d6d4d1;
  }
  * { margin: 0; padding: 0; box-sizing: border-box; }
  html, body { width: 1200px; height: 599px; overflow: hidden; background: var(--white); }
  body { position: relative; font-family: "League Spartan", "Arial Black", sans-serif; font-weight: 800; color: var(--white); }

  .tile { position: absolute; width: 233px; height: 291px; overflow: hidden; }
  .col-1 { left: 5px; } .col-2 { left: 244px; } .col-3 { left: 483px; } .col-4 { left: 722px; } .col-5 { left: 962px; }
  .row-1 { top: 5px; } .row-2 { top: 302px; }

  .band { position: absolute; left: 0; width: 100%; }
  .bg-red { background: var(--red); }
  .bg-blue { background: var(--blue); }
  .bg-white { background: var(--white); }

  .photo { position: absolute; left: 0; width: 100%; background: linear-gradient(180deg, var(--photo-light), var(--photo-mid)); }
  .photo-red { background: linear-gradient(180deg, #b8262c, #d1363a 55%, #a5222a); }
  .photo-blue { background: linear-gradient(180deg, #173a88, #2352a8 55%, #142f70); }
  .photo-kitchen { background: linear-gradient(180deg, #6d4a38, #8b6a58 45%, #d9d2cc); }

  .line { position: absolute; white-space: nowrap; line-height: 1; letter-spacing: -0.02em; }
  .center { left: 0; width: 100%; text-align: center; }
  .text-red { color: var(--red); }
  .text-blue { color: var(--blue); }
  .spaced { letter-spacing: 0.12em; }
  .wide { letter-spacing: 0.42em; }

  .price-banner { position: absolute; left: 0; top: 136px; width: 100%; height: 49px; background: rgba(209, 40, 47, 0.82); }
</style>
</head>
<body>

<!-- 1: Historic sale -->
<section class="tile col-1 row-1">
  <div class="band bg-blue" style="top:0;height:181px"></div>
  <div class="band bg-red" style="top:181px;height:110px"></div>
  <div class="line" style="left:16px;top:16px;font-size:44px">HISTORIC</div>
  <div class="line" style="left:16px;top:66px;font-size:32px">4TH OF JULY</div>
  <div class="line" style="left:16px;top:98px;font-size:74px">SALE!</div>
  <div class="line" style="left:16px;top:192px;font-size:48px">25% OFF</div>
  <div class="line" style="left:16px;top:243px;font-size:32px">EVERYTHING</div>
</section>

<!-- 2: Mega summer blowout -->
<section class="tile col-2 row-1">
  <div class="band bg-red" style="top:0;height:182px"></div>
  <div class="band bg-blue" style="top:182px;height:109px"></div>
  <div class="line" style="left:17px;top:13px;font-size:68px">MEGA</div>
  <div class="line" style="left:17px;top:81px;font-size:46px">SUMMER</div>
  <div class="line" style="left:17px;top:128px;font-size:39px">BLOWOUT!</div>
  <div class="line" style="left:17px;top:192px;font-size:48px">25% OFF</div>
  <div class="line" style="left:17px;top:243px;font-size:32px">EVERYTHING</div>
</section>

<!-- 3: One time only -->
<section class="tile col-3 row-1 bg-red">
  <div class="line" style="left:29px;top:13px;font-size:82px">ONE</div>
  <div class="line" style="left:29px;top:80px;font-size:76px">TIME</div>
  <div class="line" style="left:29px;top:144px;font-size:66px">ONLY</div>
  <div class="line" style="left:30px;top:204px;font-size:46px">25% OFF</div>
  <div class="line" style="left:30px;top:245px;font-size:32px">EVERYTHING</div>
</section>

<!-- 4: Biggest discount -->
<section class="tile col-4 row-1 bg-blue">
  <div class="line" style="left:23px;top:29px;font-size:49px">OUR</div>
  <div class="line" style="left:23px;top:72px;font-size:46px">BIGGEST</div>
  <div class="line" style="left:23px;top:116px;font-size:40px">DISCOUNT</div>
  <div class="line" style="left:23px;top:154px;font-size:40px">EVER!</div>
  <div class="line" style="left:23px;top:194px;font-size:48px">25% OFF</div>
  <div class="line" style="left:23px;top:238px;font-size:32px">EVERYTHING</div>
</section>

<!-- 5: Stock-up event -->
<section class="tile col-5 row-1">
  <div class="band bg-red" style="top:0;height:81px"></div>
  <div class="photo" style="top:81px;height:129px" role="img" aria-label="Product photo: four supplement bottles lined up on a white surface"></div>
  <div class="band bg-blue" style="top:210px;height:81px"></div>
  <div class="line" style="left:19px;top:1px;font-size:52px">25% OFF</div>
  <div class="line" style="left:19px;top:50px;font-size:23px">STOCK-UP EVENT</div>
  <div class="line" style="left:19px;top:215px;font-size:50px">25% OFF</div>
  <div class="line" style="left:19px;top:261px;font-size:20px">ALL SUPPLEMENTS</div>
</section>

<!-- 6: Biggest 4th of July sale -->
<section class="tile col-1 row-2">
  <div class="photo" style="top:0;height:150px" role="img" aria-label="Product photo: four supplement bottles on a light grey backdrop"></div>
  <div class="band bg-red" style="top:150px;height:71px"></div>
  <div class="band bg-white" style="top:221px;height:70px"></div>
  <div class="line" style="left:16px;top:159px;font-size:30px">BIGGEST 4TH</div>
  <div class="line" style="left:16px;top:191px;font-size:20px">OF JULY SALE EVER!</div>
  <div class="line text-red spaced" style="left:17px;top:228px;font-size:36px">25% OFF</div>
  <div class="line text-red wide" style="left:17px;top:261px;font-size:24px">SITEWIDE</div>
</section>

<!-- 7: July 4th mega sale -->
<section class="tile col-2 row-2">
  <div class="band bg-blue" style="top:0;height:84px"></div>
  <div class="band bg-white" style="top:84px;height:56px"></div>
  <div class="photo" style="top:140px;height:151px" role="img" aria-label="Product photo: four supplement bottles arranged at an angle"></div>
  <div class="line" style="left:19px;top:5px;font-size:42px">JULY 4TH</div>
  <div class="line" style="left:19px;top:44px;font-size:36px">MEGA SALE!</div>
  <div class="line text-blue spaced" style="left:20px;top:88px;font-size:35px">25% OFF</div>
  <div class="line text-blue wide" style="left:20px;top:120px;font-size:17px">EVERYTHING</div>
</section>

<!-- 8: Lowest prices -->
<section class="tile col-3 row-2">
  <div class="photo photo-kitchen" style="top:0;height:291px" role="img" aria-label="Photo: smiling host in a kitchen presenting a row of supplement bottles"></div>
  <div class="line center" style="top:7px;font-size:30px">THE LOWEST</div>
  <div class="line center" style="top:31px;font-size:55px">PRICES</div>
  <div class="price-banner"></div>
  <div class="line center" style="top:140px;font-size:23px">WE'VE EVER</div>
  <div class="line center" style="top:161px;font-size:21px">OFFERED! 25% OFF</div>
</section>

<!-- 9: Don't wait -->
<section class="tile col-4 row-2">
  <div class="photo photo-red" style="top:0;height:291px" role="img" aria-label="Red-tinted photo: host in a kitchen with supplement bottles on the counter"></div>
  <div class="line" style="left:26px;top:54px;font-size:56px">DON’T</div>
  <div class="line" style="left:26px;top:101px;font-size:62px">WAIT!</div>
  <div class="line" style="left:27px;top:160px;font-size:46px">25% OFF</div>
  <div class="line" style="left:27px;top:202px;font-size:30px">ENDS SOON</div>
</section>

<!-- 10: Last chance -->
<section class="tile col-5 row-2">
  <div class="photo photo-blue" style="top:0;height:291px" role="img" aria-label="Blue-tinted photo: host in a kitchen with supplement bottles on the counter"></div>
  <div class="line center" style="top:75px;font-size:27px">LAST CHANCE</div>
  <div class="line center" style="top:102px;font-size:30px">25% OFF</div>
  <div class="line center" style="top:132px;font-size:30px">TIME IS</div>
  <div class="line center" style="top:162px;font-size:30px">RUNNING</div>
  <div class="line center" style="top:192px;font-size:29px">OUT!</div>
</section>

</body>
</html>
```